Social Movement/Church Plant Website - KindAshbury.com

We need a website for our church plant startup, however we want the focus of the landing page to be around #kindashbury - that we are an organization that is FOR our town (Loveland). The site will include serving project events, social events, a place to sign up for emails, a blog, a place to give, etc. All the elements we know we want are currently at kindashbury.com . Please check this for copy.

We want this to be easy to edit as a non-developer.

I have included several logos with our colors, as well as an ai file to give you an idea of how we want the design to look and feel - also includes our branded fonts

Target Market(s)

People who live in the Northern CO area

Font styles to use
Serif
Sans Serif

Requirements
Must have
• Events (serve and social), Blog section, A place to get involved - where to give and to sign up for emails. Must match our branding colors and style hex 4c7991.
Should not have
• Should not be focused on the actual church plant on the home page. There can be some back end stuff about it, but the focus should be #kindashbury.

```html
<!DOCTYPE html>
<html lang="en">
<head>
<meta charset="utf-8">
<title>#kindashbury — For Our Town</title>
<link href="https://fonts.googleapis.com/css2?family=Montserrat:wght@400;600;700&family=Open+Sans:wght@400;600;700&display=swap" rel="stylesheet">
<style>
:root{
  --brand:#4c7991;
  --brand-dark:#3f6a80;
  --ink:#333a40;
  --muted:#6b7075;
  --light:#f2f2f2;
  --white:#ffffff;
  --dark:#1c1d1f;
}
*{margin:0;padding:0;box-sizing:border-box}
html,body{width:1200px;height:4027px;overflow:hidden}
body{font-family:"Open Sans",Arial,sans-serif;color:var(--ink);background:var(--white);position:relative}
.abs{position:absolute}
h1,h2,h3,h4,.nav,.btn{font-family:"Montserrat",Arial,sans-serif}

/* top bar */
.topbar{position:absolute;left:0;top:0;width:1200px;height:46px;background:var(--brand)}
.topbar .social{position:absolute;left:96px;top:11px;display:flex;gap:8px}
.topbar .social span{width:22px;height:22px;border:2px solid var(--white);border-radius:50%}
.topbar .phone{position:absolute;right:92px;top:14px;color:var(--white);font-size:14px;font-weight:600}

/* header */
.header{position:absolute;left:0;top:46px;width:1200px;height:84px;background:var(--white)}
.brand{position:absolute;left:90px;top:24px;font-family:"Montserrat",sans-serif;font-weight:600;font-size:28px;color:var(--dark);letter-spacing:.3px}
.nav{position:absolute;right:92px;top:36px;display:flex;gap:44px;font-size:13px;font-weight:600;color:#444}
.nav .active{color:var(--brand)}

/* hero */
.hero{position:absolute;left:0;top:130px;width:1200px;height:627px;background:radial-gradient(ellipse at 50% 70%,#7a5a48 0%,#4a3a32 45%,#262322 100%)}
.hero h1{position:absolute;left:0;width:1200px;top:282px;text-align:center;color:var(--white);font-size:48px;font-weight:700;letter-spacing:2px}
.hero .dots{position:absolute;left:44px;top:283px;display:flex;flex-direction:column;gap:8px}
.hero .dots span{width:9px;height:9px;border-radius:50%;background:rgba(255,255,255,.6)}
.hero .dots span:first-child{background:var(--white)}

/* story */
.story{position:absolute;left:0;top:757px;width:1200px;height:524px;background:var(--white)}
.story .photo{position:absolute;left:0;top:0;width:765px;height:524px;background:radial-gradient(circle at 45% 48%,#e9e4df 0%,#c9c3bd 45%,#9c948d 100%)}
.story .card{position:absolute;left:494px;top:73px;width:618px;height:378px;background:var(--white);border:4px solid var(--brand)}
.story .card-inner{position:absolute;left:18px;top:20px;width:566px;height:326px;border:2px solid var(--brand);padding:32px 28px 0 34px}
.story h2{color:var(--brand);font-size:22px;font-weight:700}
.story h3{color:var(--brand);font-size:17px;font-weight:700;margin-top:16px}
.story p{font-size:15px;line-height:27px;margin-top:10px;color:#333}
.btn{display:inline-block;background:var(--brand);color:var(--white);font-size:14px;font-weight:700;border-radius:26px;text-align:center}
.story .btn{width:156px;height:52px;line-height:52px;margin-top:24px}

/* social events */
.social-events{position:absolute;left:0;top:1281px;width:1200px;height:717px;background:linear-gradient(160deg,#2a2b2d,#141516 60%,#1d1e20)}
.section-title{position:absolute;left:0;width:1200px;text-align:center;font-size:24px;font-weight:700;letter-spacing:.5px}
.social-events .section-title{top:97px;color:var(--white)}
.social-events .sub{position:absolute;left:350px;width:500px;top:144px;text-align:center;color:var(--white);font-size:16px;font-weight:600;line-height:27px}
.event{position:absolute;top:231px;width:322px;color:var(--white);text-align:center}
.event .img{width:322px;height:193px}
.event .meta{font-size:15px;margin-top:23px}
.event h4{font-size:19px;font-weight:700;margin-top:8px}
.event p{font-size:14px;font-weight:600;line-height:26px;margin-top:8px;padding:0 14px}

/* project events */
.projects{position:absolute;left:0;top:1998px;width:1200px;height:531px;background:var(--light)}
.projects h2{position:absolute;left:89px;top:95px;font-size:22px;font-weight:700;color:var(--brand)}
.projects .intro{position:absolute;left:89px;top:138px;width:240px;font-size:15px;line-height:30px;color:#444}
.projects .lead-btn{position:absolute;left:89px;top:386px;width:142px;height:51px;line-height:51px}
.proj{position:absolute;top:83px;width:250px}
.proj .img{width:250px;height:142px}
.proj h4{font-family:"Montserrat",sans-serif;color:var(--brand);font-size:19px;font-weight:700;margin-top:32px}
.proj p{font-size:14px;line-height:26px;color:#555;margin-top:10px}
.proj .btn{width:144px;height:51px;line-height:51px;margin-top:32px}

/* testimonials */
.testimonials{position:absolute;left:0;top:2529px;width:1200px;height:392px;background:linear-gradient(180deg,#322b27,#231f1d)}
.testimonials .section-title{top:53px;color:var(--white)}
.testimonials .sub{position:absolute;left:0;width:1200px;top:96px;text-align:center;color:var(--white);font-size:16px;font-weight:600}
.avatar{position:absolute;width:56px;height:56px;border-radius:50%;background:#b9a79a;border:3px solid var(--white)}
.tname{position:absolute;color:var(--white);font-family:"Montserrat",sans-serif;font-weight:700;font-size:15px}
.quote{position:absolute;color:var(--white);font-size:12px;font-weight:600;line-height:21px;width:232px}
.qmark{position:absolute;width:24px;height:20px}
.tdots{position:absolute;left:571px;top:331px;display:flex;gap:6px}
.tdots span{width:11px;height:11px;border-radius:50%;background:#cfcfcf}
.tdots span.on{background:var(--brand);border:2px solid var(--white)}

/* blog */
.blog{position:absolute;left:0;top:2921px;width:1200px;height:712px;background:var(--white)}
.blog .section-title{top:86px;color:var(--brand)}
.blog .sub{position:absolute;left:300px;width:600px;top:132px;text-align:center;font-size:16px;line-height:27px;color:#666}
.post{position:absolute;top:210px;width:320px;height:421px;background:var(--white);box-shadow:0 2px 10px rgba(0,0,0,.12)}
.post .img{width:320px;height:207px}
.post .body{padding:26px 14px 0 14px}
.post h4{font-family:"Montserrat",sans-serif;color:var(--brand);font-size:20px;font-weight:700}
.post .by{font-size:12px;color:#666;margin-top:10px}
.post p{font-size:12px;line-height:20px;color:#555;margin-top:10px}
.post .stats{display:flex;gap:18px;align-items:center;font-size:12px;color:#555;margin-top:16px}
.post .stats span{display:flex;align-items:center;gap:5px}

/* footer */
.footer{position:absolute;left:0;top:3633px;width:1200px;height:394px;background:var(--brand);color:var(--white)}
.fcol{position:absolute;top:93px}
.fcol h4{font-size:14px;font-weight:700;letter-spacing:.5px}
.fcol p,.fcol li{font-size:13px;line-height:25px;font-weight:600}
.fcol .txt{margin-top:24px}
.fcol ul{list-style:none;margin-top:24px}
.fcol li{display:flex;align-items:center;gap:14px;line-height:31px}
.fcol li::before{content:"";width:9px;height:9px;border-radius:50%;background:var(--white)}
.fsocial{position:absolute;left:95px;top:268px;display:flex;gap:8px}
.fsocial span{width:30px;height:30px;border-radius:50%;background:#1f2b33}
.newsletter{display:flex;margin-top:20px}
.newsletter .field{width:196px;height:40px;background:var(--white);color:#777;font-size:11px;line-height:40px;padding-left:12px}
.newsletter .go{width:40px;height:40px;background:#1f2b33;display:flex;align-items:center;justify-content:center}
.copy{position:absolute;left:0;width:1200px;top:354px;text-align:center;font-size:12px;font-weight:600;letter-spacing:.3px}
</style>
</head>
<body>

<div class="topbar">
  <div class="social"><span></span><span></span><span></span><span></span></div>
  <div class="phone">Phone: +1 970 555 0142</div>
</div>

<header class="header">
  <div class="brand">#kindashbury</div>
  <nav class="nav">
    <span class="active">HOME</span><span>ABOUT</span><span>EVENTS</span><span>BLOG</span><span>GIVE</span><span>CONTACT US</span>
  </nav>
</header>

<section class="hero" role="img" aria-label="Friends sharing a meal together around a table">
  <div class="dots"><span></span><span></span><span></span></div>
  <h1># KINDASHBURY</h1>
</section>

<section class="story">
  <div class="photo" role="img" aria-label="Circle of hands joined together from above"></div>
  <div class="card">
    <div class="card-inner">
      <h2>OUR STORY</h2>
      <h3>Working Toward a Better Tomorrow</h3>
      <p>What if we were known not by what we're against, but by what we're for? &nbsp;If our collective energy was invested in things that unite rather than divide, wouldn't we see stronger neighborhoods, healthier communities, and more resilient relationships? &nbsp;We believe so.</p>
      <span class="btn">READ MORE</span>
    </div>
  </div>
</section>

<section class="social-events">
  <h2 class="section-title">SOCIAL EVENTS</h2>
  <p class="sub">At vero eos et accusamus et iusto odio dignissimos ducimus qui blanditiis</p>

  <article class="event" style="left:97px">
    <div class="img" role="img" aria-label="Volunteers working together outdoors" style="background:linear-gradient(135deg,#5f8f3e,#2e5a22)"></div>
    <div class="meta">John Doe | June 20, 2018</div>
    <h4>At vero eos et</h4>
    <p>At vero eos et accusamus et iusto odio dignissimos ducimus qui blanditiis praesentium voluptatum deleniti atque corrupti quos</p>
  </article>
  <article class="event" style="left:440px">
    <div class="img" role="img" aria-label="Friends sharing pizza at a social gathering" style="background:linear-gradient(135deg,#8a7a66,#4b5a4a)"></div>
    <div class="meta">John Doe | June 20, 2018</div>
    <h4>At vero eos et</h4>
    <p>At vero eos et accusamus et iusto odio dignissimos ducimus qui blanditiis praesentium voluptatum deleniti atque corrupti quos</p>
  </article>
  <article class="event" style="left:784px">
    <div class="img" role="img" aria-label="Group playing games on a grass field" style="background:linear-gradient(180deg,#7f8d7a,#4f6b3a)"></div>
    <div class="meta">John Doe | June 20, 2018</div>
    <h4>At vero eos et</h4>
    <p>At vero eos et accusamus et iusto odio dignissimos ducimus qui blanditiis praesentium voluptatum deleniti atque corrupti quos</p>
  </article>
</section>

<section class="projects">
  <h2>PROJECT EVENTS</h2>
  <p class="intro">We are for the broken and the brand new, the beautifully painted and the terribly stained. &nbsp;We are for the addict and the aristocrat, the put together and the never been messier.</p>
  <span class="btn lead-btn">READ MORE</span>

  <article class="proj" style="left:352px">
    <div class="img" role="img" aria-label="Volunteers sorting donations at a table" style="background:linear-gradient(135deg,#7c8f9c,#4e5f6a)"></div>
    <h4>At vero eos et</h4>
    <p>Sed ut perspiciatis unde omnis iste natus error sit voluptatem accusantium doloremque laudan-</p>
    <span class="btn">READ MORE</span>
  </article>
  <article class="proj" style="left:607px">
    <div class="img" role="img" aria-label="Smiling volunteer at a service project" style="background:linear-gradient(135deg,#6aa3a0,#9a8372)"></div>
    <h4>At vero eos et</h4>
    <p>Sed ut perspiciatis unde omnis iste natus error sit voluptatem accusantium doloremque laudan-</p>
    <span class="btn">READ MORE</span>
  </article>
  <article class="proj" style="left:862px">
    <div class="img" role="img" aria-label="Neighbors of all ages serving together" style="background:linear-gradient(135deg,#a9a79c,#6e7a63)"></div>
    <h4>At vero eos et</h4>
    <p>Sed ut perspiciatis unde omnis iste natus error sit voluptatem accusantium doloremque laudan-</p>
    <span class="btn">READ MORE</span>
  </article>
</section>

<section class="testimonials">
  <h2 class="section-title">TESTIMONIALS</h2>
  <p class="sub">At vero eos et accusamus et</p>

  <div class="avatar" role="img" aria-label="Portrait of John" style="left:98px;top:179px"></div>
  <div class="tname" style="left:166px;top:198px">JOHN</div>
  <svg class="qmark" style="left:297px;top:146px" viewBox="0 0 24 20"><path fill="#fff" d="M0 20V11C0 4 3 1 9 0v4c-3 1-4 3-4 6h4v10zM14 20V11c0-7 3-10 9-11v4c-3 1-4 3-4 6h4v10z"/></svg>
  <p class="quote" style="left:295px;top:207px">Lorem ipsum dolor sit amet, consectetur adipisicing elit. Earum totam est, veritatis cumque, officia maxime aut</p>
  <svg class="qmark" style="left:543px;top:249px" viewBox="0 0 24 20"><path fill="#fff" d="M24 0v9c0 7-3 10-9 11v-4c3-1 4-3 4-6h-4V0zM10 0v9c0 7-3 10-9 11v-4c3-1 4-3 4-6H1V0z"/></svg>

  <div class="avatar" role="img" aria-label="Portrait of David" style="left:632px;top:179px"></div>
  <div class="tname" style="left:700px;top:198px">DAVID</div>
  <svg class="qmark" style="left:806px;top:146px" viewBox="0 0 24 20"><path fill="#fff" d="M0 20V11C0 4 3 1 9 0v4c-3 1-4 3-4 6h4v10zM14 20V11c0-7 3-10 9-11v4c-3 1-4 3-4 6h4v10z"/></svg>
  <p class="quote" style="left:806px;top:207px">Lorem ipsum dolor sit amet, consectetur adipisicing elit. Earum totam est, veritatis cumque, officia maxime aut</p>
  <svg class="qmark" style="left:1077px;top:249px" viewBox="0 0 24 20"><path fill="#fff" d="M24 0v9c0 7-3 10-9 11v-4c3-1 4-3 4-6h-4V0zM10 0v9c0 7-3 10-9 11v-4c3-1 4-3 4-6H1V0z"/></svg>

  <div class="tdots"><span></span><span></span><span class="on"></span><span></span></div>
</section>

<section class="blog">
  <h2 class="section-title">LATEST BLOG</h2>
  <p class="sub">Lorem ipsum dolor sit amet, consectetur adipisicing elit. Earum totam est, veritatis cumque, officia maxime aut labore provident</p>

  <article class="post" style="left:94px">
    <div class="img" role="img" aria-label="Volunteers in matching shirts at a food drive" style="background:linear-gradient(135deg,#c0794a,#4f86b0)"></div>
    <div class="body">
      <h4>Let's Move With Blog</h4>
      <div class="by">Post by: Z Lopez &nbsp;In: Garden Maker</div>
      <p>Lorem ipsum dolor sit amet, consectetur adipisicing elit. Ipsam inventore, fuga soluta. Aperiam?</p>
      <div class="stats">
        <span><svg width="11" height="11" viewBox="0 0 11 11"><rect x=".5" y="1.5" width="10" height="9" fill="none" stroke="#777"/><line x1=".5" y1="4" x2="10.5" y2="4" stroke="#777"/></svg>25 May 2018</span>
        <span><svg width="12" height="11" viewBox="0 0 12 11"><ellipse cx="6" cy="5" rx="5.5" ry="4.2" fill="none" stroke="#777"/></svg>250</span>
        <span><svg width="11" height="11" viewBox="0 0 11 11"><circle cx="2" cy="5.5" r="1.5" fill="#777"/><circle cx="9" cy="2" r="1.5" fill="#777"/><circle cx="9" cy="9" r="1.5" fill="#777"/><path d="M2 5.5L9 2M2 5.5L9 9" stroke="#777"/></svg>350</span>
      </div>
    </div>
  </article>
  <article class="post" style="left:440px">
    <div class="img" role="img" aria-label="Colorful volunteer sign on a painted wall" style="background:linear-gradient(135deg,#8fa5ad,#c9b9a4)"></div>
    <div class="body">
      <h4>Let's Move With Blog</h4>
      <div class="by">Post by: Z Lopez &nbsp;In: Garden Maker</div>
      <p>Lorem ipsum dolor sit amet, consectetur adipisicing elit. Ipsam inventore, fuga soluta. Aperiam?</p>
      <div class="stats">
        <span><svg width="11" height="11" viewBox="0 0 11 11"><rect x=".5" y="1.5" width="10" height="9" fill="none" stroke="#777"/><line x1=".5" y1="4" x2="10.5" y2="4" stroke="#777"/></svg>25 May 2018</span>
        <span><svg width="12" height="11" viewBox="0 0 12 11"><ellipse cx="6" cy="5" rx="5.5" ry="4.2" fill="none" stroke="#777"/></svg>250</span>
        <span><svg width="11" height="11" viewBox="0 0 11 11"><circle cx="2" cy="5.5" r="1.5" fill="#777"/><circle cx="9" cy="2" r="1.5" fill="#777"/><circle cx="9" cy="9" r="1.5" fill="#777"/><path d="M2 5.5L9 2M2 5.5L9 9" stroke="#777"/></svg>350</span>
      </div>
    </div>
  </article>
  <article class="post" style="left:787px">
    <div class="img" role="img" aria-label="Hands stacked together in unity" style="background:linear-gradient(135deg,#e2cdb8,#a9765a)"></div>
    <div class="body">
      <h4>Let's Move With Blog</h4>
      <div class="by">Post by: Z Lopez &nbsp;In: Garden Maker</div>
      <p>Lorem ipsum dolor sit amet, consectetur adipisicing elit. Ipsam inventore, fuga soluta. Aperiam?</p>
      <div class="stats">
        <span><svg width="11" height="11" viewBox="0 0 11 11"><rect x=".5" y="1.5" width="10" height="9" fill="none" stroke="#777"/><line x1=".5" y1="4" x2="10.5" y2="4" stroke="#777"/></svg>25 May 2018</span>
        <span><svg width="12" height="11" viewBox="0 0 12 11"><ellipse cx="6" cy="5" rx="5.5" ry="4.2" fill="none" stroke="#777"/></svg>250</span>
        <span><svg width="11" height="11" viewBox="0 0 11 11"><circle cx="2" cy="5.5" r="1.5" fill="#777"/><circle cx="9" cy="2" r="1.5" fill="#777"/><circle cx="9" cy="9" r="1.5" fill="#777"/><path d="M2 5.5L9 2M2 5.5L9 9" stroke="#777"/></svg>350</span>
      </div>
    </div>
  </article>
</section>

<footer class="footer">
  <div class="fcol" style="left:102px;width:210px">
    <h4>INFORMATION</h4>
    <p class="txt">Sed ut perspiciatis unde omnis iste natus eiantium, totam rem aperiam, eaque ipsa architecto explicabo.</p>
  </div>
  <div class="fsocial"><span></span><span></span><span></span><span></span></div>

  <div class="fcol" style="left:376px;width:220px">
    <h4>CONTACT US</h4>
    <p class="txt">NO:10, 123 street,<br>Location, CO 1051<br>Phone: &nbsp;+1 970 555 0142<br>Email: &nbsp;&nbsp;info@kindashbury.com</p>
  </div>

  <div class="fcol" style="left:642px;width:200px">
    <h4>FEATURE SERVICES</h4>
    <ul>
      <li>Privacy policy</li>
      <li>Faq</li>
      <li>partner With Us</li>
      <li>Events</li>
      <li>Request A Speaker</li>
    </ul>
  </div>

  <div class="fcol" style="left:878px;width:240px">
    <h4>NEWSLETTER</h4>
    <p class="txt">But I must explain to you how all this mistaken idea of denouncing pleasure and praising</p>
    <div class="newsletter">
      <div class="field">Enter your email address</div>
      <div class="go"><svg width="12" height="12" viewBox="0 0 12 12"><path d="M2 6h8M7 3l3 3-3 3" stroke="#fff" stroke-width="1.6" fill="none"/></svg></div>
    </div>
  </div>

  <div class="copy">© 2018 KINDASHBURY | ALL RIGHTS RESERVED.</div>
</footer>

</body>
</html>
```